a residential painting contractor I need a 6x9 postcard made

I already have a logo, I'm trying to offer my services to people. you can put that there's a 250$ discount for first time customers. include my License number #4627381 as well as the services I offer, interior and exterior painting, pressure washing, cabinet painting, epoxy floors, wood staining, decks, fences and much more. I'm licensed bonded and insured as well.

Target Market(s)

residential consumers (homeowners)

Industry/Entity Type

Painting contractor

Requirements
Must have
• postage stuff on the back I've linked some pictures top right please, my license number, what I do, phone number (555)317-0846 email velbrushworks7@mailzo.net, front and back of postcard
Nice to have
• well lit house in the background, maybe little circles of people doing some of the services I offer

```html
<!DOCTYPE html>
<html lang="en">
<head>
<meta charset="utf-8">
<title>Velbrush Works – Postcard</title>
<link href="https://fonts.googleapis.com/css2?family=Montserrat:wght@300;400;500;700;800&display=swap" rel="stylesheet">
<style>
:root{
  --canvas:#ffffff;
  --ink:#1c1c1c;
  --charcoal:#262626;
  --black:#151515;
  --band:#4a4a4a;
  --muted:#9c9c9c;
  --paper:#f7f7f7;
  --white:#ffffff;
  --chip-dark:#7b7b7b;
  --chip-light:#d9d9d9;
  --stamp:#e4e4e4;
}
*{margin:0;padding:0;box-sizing:border-box}
html,body{width:1200px;height:2366px;overflow:hidden;background:var(--canvas)}
body{font-family:"Montserrat",Arial,sans-serif;color:var(--white);position:relative}
.card{position:absolute;left:50px;width:1100px;height:733px;overflow:hidden;box-shadow:0 6px 18px rgba(0,0,0,.28)}
.card--front{top:400px;background:var(--charcoal)}
.card--back{top:1233px;background:var(--white)}
.layer{position:absolute}

/* front */
.top-band{left:520px;top:0;width:580px;height:110px;background:var(--band);
  clip-path:polygon(4% 0,100% 0,100% 100%,0 100%,3% 70%,1% 45%,5% 20%)}
.house-photo{left:260px;top:40px;width:640px;height:580px;
  background:linear-gradient(160deg,#3a3a3a 0%,#2a2a2a 55%,#1e1e1e 100%);opacity:.85}
.couple-photo{left:560px;top:60px;width:540px;height:673px;
  background:linear-gradient(180deg,#dfe3e1 0%,#d3d6d4 60%,#b89a80 85%,#9c7e66 100%);
  clip-path:polygon(18% 4%,40% 2%,60% 0,80% 3%,100% 1%,100% 100%,20% 100%,22% 94%,16% 88%,20% 80%,14% 72%,18% 64%,12% 55%,17% 47%,10% 38%,16% 30%,12% 20%,19% 12%)}
.bottom-paper{left:0;top:610px;width:760px;height:123px;background:var(--paper);
  clip-path:polygon(0 25%,10% 18%,25% 22%,40% 12%,55% 16%,70% 8%,85% 14%,92% 0,96% 40%,92% 70%,100% 100%,0 100%)}
.name-tab{left:62px;top:0;width:211px;height:235px;background:var(--white);
  border-radius:0 0 106px 106px;display:flex;flex-direction:column;align-items:center;justify-content:center;gap:6px}
.brand-name{font-weight:800;font-size:26px;line-height:1.05;color:var(--ink);text-align:center;letter-spacing:.5px}
.brand-dot{width:14px;height:14px;border-radius:50%;background:var(--ink)}
.headline{left:62px;top:262px;font-weight:800;font-size:58px;line-height:56px;text-transform:uppercase;letter-spacing:-.5px}
.headline .soft{color:var(--muted)}
.dots{display:flex;gap:6px}
.dots span{width:9px;height:9px;border-radius:50%;background:var(--white)}
.dots span+span{background:var(--muted)}
.dots span:last-child{background:#5d5d5d}
.front-dots{left:64px;top:498px}
.license{left:62px;top:528px;width:460px;text-align:right;font-weight:300;font-size:17px;color:#cfcfcf}
.offer{display:flex;height:86px;align-items:stretch}
.offer-amount{background:var(--chip-dark);color:var(--white);font-weight:700;font-size:54px;display:flex;align-items:center;padding:0 14px;letter-spacing:-1px}
.offer-amount sup{font-size:22px;margin-right:2px;align-self:flex-start;margin-top:16px}
.offer-text{background:var(--chip-light);color:var(--ink);flex:1;display:flex;flex-direction:column;justify-content:center;padding-left:16px;border-left:3px solid #9a9a9a;font-size:25px;line-height:28px;text-transform:uppercase}
.offer-text b{font-weight:800}
.offer-text span{font-weight:300}
.front-offer{left:62px;top:562px;width:460px}
.contact{display:flex;align-items:center;gap:30px;font-size:19px;color:var(--ink)}
.contact-item{display:flex;align-items:center;gap:10px}
.contact-item svg{width:20px;height:20px}
.contact .phone{font-weight:700}
.front-contact{left:62px;top:680px}

/* back */
.crew-photo{left:0;top:0;width:600px;height:290px;
  background:linear-gradient(90deg,#3c8f3c 0%,#4fa34f 35%,#8ea0b4 60%,#b9bcc3 100%);
  clip-path:polygon(0 0,100% 0,97% 20%,93% 35%,88% 52%,80% 70%,70% 80%,55% 74%,40% 78%,25% 73%,10% 78%,0 72%)}
.dark-panel{left:0;top:200px;width:620px;height:533px;background:var(--black);
  clip-path:polygon(0 10%,12% 6%,28% 8%,45% 3%,62% 5%,75% 0,82% 8%,78% 18%,85% 28%,80% 40%,88% 50%,84% 62%,90% 72%,86% 84%,92% 100%,0 100%)}
.services-title{left:62px;top:285px;font-weight:800;font-size:32px;text-transform:uppercase}
.back-dots{left:64px;top:330px}
.service-list{list-style:none;display:flex;flex-direction:column;gap:14px}
.service{display:flex;align-items:center;gap:12px;font-size:17px;line-height:20px;color:#eaeaea}
.service-icon{width:32px;height:32px;border-radius:50%;background:#5c5c5c;display:flex;align-items:center;justify-content:center;flex-shrink:0}
.service-icon i{width:12px;height:12px;border:2px solid #d0d0d0;border-radius:2px}
.services-left{left:62px;top:360px}
.services-right{left:292px;top:363px}
.back-offer{left:62px;top:565px;width:412px;border:2px dashed #8a8a8a;padding:4px;background:#2a2a2a}
.back-offer .offer{height:68px}
.back-offer .offer-amount{font-size:46px}
.back-offer .offer-text{font-size:21px;line-height:23px}
.back-contact{left:62px;top:686px}
.back-contact .contact-item{color:var(--white);font-size:17px}
.mail-brand{left:650px;top:100px;width:210px;display:flex;flex-direction:column;align-items:center;gap:8px}
.mail-brand .brand-name{font-size:22px}
.stamp-box{left:916px;top:58px;width:124px;height:122px;background:var(--stamp)}
</style>
</head>
<body>

<section class="card card--front" aria-label="Postcard front">
  <div class="layer top-band"></div>
  <div class="layer house-photo" role="img" aria-label="Dim photo of a two-storey house behind the headline"></div>
  <div class="layer couple-photo" role="img" aria-label="Photo of a smiling couple holding paint rollers in a freshly painted room"></div>
  <div class="layer bottom-paper"></div>

  <div class="layer name-tab">
    <span class="brand-dot"></span>
    <p class="brand-name">VELBRUSH<br>WORKS</p>
  </div>

  <h1 class="layer headline">
    <span class="soft">We are<br>residential</span><br>Painting<br>contractor
  </h1>
  <div class="layer dots front-dots"><span></span><span></span><span></span></div>

  <p class="layer license">LICENSE NUMBER #4627381</p>

  <div class="layer offer front-offer">
    <div class="offer-amount"><sup>$</sup>250</div>
    <div class="offer-text"><b>Discount for</b><span>First time customers</span></div>
  </div>

  <div class="layer contact front-contact">
    <span class="contact-item phone">
      <svg viewBox="0 0 24 24"><path d="M6.6 3.5l3 3.2-2 2.2c1.2 2.6 3.3 4.7 5.9 5.9l2.2-2 3.2 3-1.8 3.2C11.3 19.5 4.5 12.7 3.4 5.3z" fill="none" stroke="#1c1c1c" stroke-width="2" stroke-linejoin="round"/></svg>
      (555)317-0846
    </span>
    <span class="contact-item">
      <svg viewBox="0 0 24 24"><g fill="none" stroke="#1c1c1c" stroke-width="1.8"><circle cx="12" cy="12" r="9"/><ellipse cx="12" cy="12" rx="4" ry="9"/><path d="M3 12h18M5 7h14M5 17h14"/></g></svg>
      velbrushworks7@mailzo.net
    </span>
  </div>
</section>

<section class="card card--back" aria-label="Postcard back">
  <div class="layer crew-photo" role="img" aria-label="Photo of two workers in hard hats painting an exterior wall green"></div>
  <div class="layer dark-panel"></div>

  <h2 class="layer services-title">Our services</h2>
  <div class="layer dots back-dots"><span></span><span></span><span></span></div>

  <ul class="layer service-list services-left">
    <li class="service"><span class="service-icon"><i></i></span>Interior and<br>exterior painting</li>
    <li class="service"><span class="service-icon"><i></i></span>Pressure washing</li>
    <li class="service"><span class="service-icon"><i></i></span>Cabinet painting</li>
    <li class="service"><span class="service-icon"><i></i></span>Epoxy floors</li>
  </ul>
  <ul class="layer service-list services-right">
    <li class="service"><span class="service-icon"><i></i></span>Wood staining</li>
    <li class="service"><span class="service-icon"><i></i></span>Decks</li>
    <li class="service"><span class="service-icon"><i></i></span>Fences</li>
  </ul>

  <div class="layer back-offer">
    <div class="offer">
      <div class="offer-amount"><sup>$</sup>250</div>
      <div class="offer-text"><b>Discount for</b><span>First time customers</span></div>
    </div>
  </div>

  <div class="layer contact back-contact">
    <span class="contact-item phone">
      <svg viewBox="0 0 24 24"><path d="M6.6 3.5l3 3.2-2 2.2c1.2 2.6 3.3 4.7 5.9 5.9l2.2-2 3.2 3-1.8 3.2C11.3 19.5 4.5 12.7 3.4 5.3z" fill="none" stroke="#ffffff" stroke-width="2" stroke-linejoin="round"/></svg>
      (555)317-0846
    </span>
    <span class="contact-item">
      <svg viewBox="0 0 24 24"><g fill="none" stroke="#ffffff" stroke-width="1.8"><circle cx="12" cy="12" r="9"/><ellipse cx="12" cy="12" rx="4" ry="9"/><path d="M3 12h18M5 7h14M5 17h14"/></g></svg>
      velbrushworks7@mailzo.net
    </span>
  </div>

  <div class="layer mail-brand">
    <span class="brand-dot"></span>
    <p class="brand-name">VELBRUSH<br>WORKS</p>
  </div>
  <div class="layer stamp-box" aria-label="Postage area"></div>
</section>

</body>
</html>
```